Modern Attractive Letterhead for Veterinary House Call Business.

A letterhead which can be printed on A4, A5 and A6 paper sizes.
To have: ( our files to be uploaded)
1. Logo with Text
2. telephone
3. email
4. website
5. Address

Target Market(s)

60-85year mainly women pet owners. Also market include families, young professionals, busy people who have dogs and cats

Industry/Entity Type

Business

Requirements
Must have
• 1. Logo with Text ( provided)
• 2. telephone
• 3. email
• 4. website
• 5. Address
Nice to have
• Needs to be modern, preferably warm and caring in nature( if possible )
Should not have
• difficulty in printing A5 and A6

```html
<!DOCTYPE html>
<html lang="en">
<head>
<meta charset="utf-8">
<title>Kindred Pet Care — Letterhead</title>
<link rel="stylesheet" href="https://fonts.googleapis.com/css2?family=Marcellus&display=swap">
<style>
  :root {
    --green: #3f9a3a;
    --blue: #2a6fb5;
    --brand-blue: #1d5ea8;
    --ink: #2b2b2b;
    --rule: #9a9a9a;
    --paper-top: #ffffff;
    --paper-bottom: #f1f1f3;
  }
  * { margin: 0; padding: 0; box-sizing: border-box; }
  html, body { width: 948px; height: 1200px; overflow: hidden; background: #ffffff; }
  .letterhead {
    position: relative;
    width: 948px;
    height: 1200px;
    background: linear-gradient(160deg, var(--paper-top) 30%, var(--paper-bottom) 100%);
    font-family: "Marcellus", Georgia, serif;
    color: var(--ink);
  }
  .brand {
    position: absolute;
    left: 34px;
    top: 40px;
    display: flex;
    align-items: center;
    gap: 16px;
  }
  .brand-dot {
    width: 64px;
    height: 64px;
    border-radius: 50%;
    background: var(--brand-blue);
  }
  .brand-name {
    font-size: 40px;
    font-weight: 400;
    color: var(--brand-blue);
    white-space: nowrap;
  }
  .contact {
    position: absolute;
    left: 666px;
    top: 50px;
    padding-left: 9px;
    border-left: 1px solid var(--rule);
    list-style: none;
  }
  .contact li {
    display: flex;
    align-items: center;
    gap: 7px;
    height: 21px;
    font-size: 13.5px;
    letter-spacing: 0.3px;
    white-space: nowrap;
  }
  .contact svg { width: 13px; height: 13px; flex: none; }
  .contact .upper { text-transform: uppercase; }
  .address {
    position: absolute;
    right: 26px;
    top: 1150px;
    font-size: 16px;
    letter-spacing: 0.6px;
  }
  .footer-band {
    position: absolute;
    left: 0;
    bottom: 0;
    width: 948px;
    height: 12px;
    display: flex;
  }
  .footer-band .band-green { flex: 1; background: var(--green); }
  .footer-band .band-blue { flex: 1; background: var(--blue); }
</style>
</head>
<body>
<main class="letterhead">
  <header class="brand">
    <span class="brand-dot"></span>
    <span class="brand-name">Kindred Pet Care</span>
  </header>

  <ul class="contact">
    <li>
      <svg viewBox="0 0 16 16" aria-hidden="true"><circle cx="8" cy="8" r="7.2" fill="none" stroke="var(--green)" stroke-width="1.2"/><path d="M5.3 4.2l1.4-.3.8 2-1 .8c.5 1.1 1.3 1.9 2.3 2.4l.8-1 2 .8-.3 1.5c-3.3.3-6.4-2.8-6-6.2z" fill="var(--green)"/></svg>
      <span>0400 123 456</span>
    </li>
    <li>
      <svg viewBox="0 0 16 16" aria-hidden="true"><rect x="1" y="3.5" width="14" height="9.5" rx="1.5" fill="var(--green)"/><path d="M1.8 4.5L8 9l6.2-4.5" fill="none" stroke="#fff" stroke-width="1.3"/></svg>
      <span class="upper">hello@kindredpetcare.com.au</span>
    </li>
    <li>
      <svg viewBox="0 0 16 16" aria-hidden="true"><g fill="none" stroke="var(--green)" stroke-width="1.2"><circle cx="8" cy="8" r="6.8"/><ellipse cx="8" cy="8" rx="3" ry="6.8"/><path d="M1.2 8h13.6M2.4 4.5h11.2M2.4 11.5h11.2"/></g></svg>
      <span class="upper">www.kindredpetcare.com.au</span>
    </li>
  </ul>

  <p class="address">PO Box 4410 Riverbend QLD 4170</p>

  <div class="footer-band" aria-hidden="true">
    <span class="band-green"></span>
    <span class="band-blue"></span>
  </div>
</main>
</body>
</html>
```